Property investment company needs a letterhead design!

We are a new residential and commercial property investment company. Name of the company is Morvessa Group, LLC. We have a new logo and now we need letterhead! We prefer to have a professional and upscale appearance. We don't have any fixed requirements, so be creative! Thank you for considering this project. We are so excited to see what happens!

Target Market(s)

Professional

Industry/Entity Type

Real Estate Development

```html
<!DOCTYPE html>
<html lang="en">
<head>
<meta charset="utf-8">
<title>Morvessa Group, LLC — Letterhead</title>
<link rel="stylesheet" href="https://fonts.googleapis.com/css2?family=Source+Sans+3:wght@400;700&display=swap">
<style>
  :root {
    --brand-green: #8cc63f;
    --brand-green-deep: #3f9a3a;
    --brand-navy: #0e2340;
    --brand-blue: #1a4a8a;
    --ink: #111111;
    --paper: #ffffff;
  }
  html, body {
    margin: 0;
    padding: 0;
    background: var(--paper);
    overflow: hidden;
  }
  .letterhead {
    position: relative;
    width: 927px;
    height: 1200px;
    overflow: hidden;
    background: var(--paper);
    font-family: "Source Sans 3", "Myriad Pro", sans-serif;
    color: var(--ink);
  }
  .letterhead__art {
    position: absolute;
    inset: 0;
    width: 927px;
    height: 1200px;
  }
  .brand-name {
    position: absolute;
    left: 26px;
    top: 62px;
    width: 200px;
    margin: 0;
    text-align: center;
    font-weight: 700;
    font-size: 27px;
    line-height: 30px;
    letter-spacing: 0.5px;
    color: var(--brand-navy);
    text-transform: uppercase;
  }
  .letter-body {
    position: absolute;
    left: 43px;
    top: 275px;
    width: 840px;
    font-size: 19px;
    line-height: 26.6px;
    letter-spacing: -0.1px;
  }
  .letter-body p {
    margin: 0 0 26.6px;
  }
  .letter-body p.tight {
    margin-bottom: 0;
  }
  .contact-bar {
    position: absolute;
    top: 1147px;
    left: 0;
    width: 927px;
    height: 20px;
    font-size: 13.5px;
    line-height: 20px;
    color: var(--paper);
  }
  .contact-bar span {
    position: absolute;
    top: 0;
    white-space: nowrap;
  }
  .contact-bar .contact-phone { left: 273px; }
  .contact-bar .contact-web { left: 469px; }
  .contact-bar .contact-address { left: 683px; }
</style>
</head>
<body>
<div class="letterhead">
  <svg class="letterhead__art" viewBox="0 0 927 1200" aria-hidden="true">
    <defs>
      <linearGradient id="footer-band" x1="0" y1="0" x2="1" y2="0">
        <stop offset="0" stop-color="#0c1d3a"/>
        <stop offset="1" stop-color="#1a4a8a"/>
      </linearGradient>
      <linearGradient id="tab-green" x1="0" y1="0" x2="1" y2="1">
        <stop offset="0" stop-color="#8cc63f"/>
        <stop offset="1" stop-color="#2f8a3a"/>
      </linearGradient>
    </defs>
    <!-- header green field -->
    <path class="header-field" fill="var(--brand-green)"
          d="M0 0 H760 C560 70 300 150 0 252 Z"/>
    <!-- header navy swoosh -->
    <path class="header-swoosh" fill="var(--brand-navy)"
          d="M125 206 C330 110 560 30 720 0 H927 V94 C700 110 420 130 125 206 Z"/>
    <!-- thin green crescent within swoosh -->
    <path class="header-crescent" fill="var(--brand-green)"
          d="M406 112 C600 70 780 52 927 46 V62 C780 66 600 84 406 112 Z"/>
    <!-- footer band -->
    <rect class="footer-band" x="150" y="1119" width="777" height="81" fill="url(#footer-band)"/>
    <!-- footer tabs -->
    <path class="footer-tab" fill="url(#tab-green)" stroke="url(#tab-green)" stroke-width="16" stroke-linejoin="round"
          d="M8 1048 L150 1176 L150 1200 L8 1200 Z"/>
    <path class="footer-tab" fill="url(#tab-green)" stroke="url(#tab-green)" stroke-width="16" stroke-linejoin="round"
          d="M120 1086 L190 1122 L180 1200 L88 1200 L88 1125 Z"/>
  </svg>

  <h1 class="brand-name">Morvessa<br>Group, LLC</h1>

  <div class="letter-body">
    <p>Name<br>Title<br>Company<br>Address<br>City, State Zip Code</p>
    <p>Greeting (Salutation Examples)</p>
    <p>Dear Mr./Ms. Last Name:<br>
    Use a formal salutation, not a first name, unless you know the person well.<br>
    If you do not know the person's gender, you can write out their full name.<br>
    For instance, "Dear Pat Crody" instead of "Dear Mr. Crody" or "Dear Ms.<br>
    Crody." If you do not know the recipient’s name, it’s still common and<br>
    acceptable to use the old-fashioned “To Whom It May Concern.”</p>
    <p>Body of Letter</p>
    <p>The first paragraph of your letter should provide an introduction as to why you are<br>
    writing so that your reason for contacting the person is obvious from the beginning.<br>
    Then, in the following paragraphs, provide specific details about your request or the<br>
    information you are providing.<br>
    The last paragraph of your letter should reiterate the reason you are writing and thank<br>
    the reader for reviewing your request. If appropriate, it should also politely ask for a<br>
    written response or for the opportunity to arrange a meeting to further discuss your request.<br>
    Closing</p>
    <p class="tight">Best regards, (Closing Examples)</p>
  </div>

  <div class="contact-bar">
    <span class="contact-phone">+ 012 345 678 90</span>
    <span class="contact-web">www.yourname.com</span>
    <span class="contact-address">1480 Larkspur Lane - New York</span>
  </div>
</div>
</body>
</html>
```